The Vixen Rides Again Line of Sparkling Wine & Spirits

Back info: Tara Rose Whitfield Owner 209-555-0143 1480 E. Harlow Rd, Bldg. 7, & 8, Lodi Ca. 95299
Sparkling Wines & Memorabilia www.thevixenridesagain.example
Ok I have uploaded the winning design. The color that I am after is the Fushia, Raspberry, Red, Matte Satin Matalic Finish. With a 24 Karet Gold color Foil. The Bottle is on the top row and it's the 2nd Bottle in. That is the Color that I want. This is the style of font. Make sure that you put what we're advertising. Good Luck to you all. Warmest regards, Tara
Target Market(s)
21 & up UniSex
Industry/Entity Type
Sparkling Wine and Memorabilia
Contact Information for Business Card
there listed up above.....

```html
<!DOCTYPE html>
<html lang="en">
<head>
<meta charset="utf-8">
<title>The Vixen Rides Again – Business Card</title>
<link rel="stylesheet" href="https://fonts.googleapis.com/css2?family=Arimo:wght@400;700&family=Courgette&display=swap">
<style>
  :root{
    --stage:#2b2b2b;
    --fuchsia:#e0158f;
    --fuchsia-deep:#c70f7c;
    --gold:#f2c21b;
    --ink:#111111;
    --white:#ffffff;
    --card-black:#141414;
    --card-black-mid:#1f1f1f;
    --card-black-soft:#3a3a3a;
  }
  *{box-sizing:border-box;margin:0;padding:0}
  html,body{width:1200px;height:800px;overflow:hidden;background:var(--stage)}
  .canvas{
    position:relative;width:1200px;height:800px;
    display:flex;align-items:center;justify-content:center;gap:50px;
  }
  .card{
    position:relative;width:525px;height:300px;border-radius:14px;overflow:hidden;
    box-shadow:0 10px 30px rgba(0,0,0,.45);
  }

  /* front */
  .card-front{
    background:radial-gradient(ellipse at 55% 55%, var(--fuchsia) 0%, var(--fuchsia-deep) 100%);
  }
  .front-texture{
    position:absolute;inset:0;
    background:linear-gradient(160deg, rgba(255,255,255,.08), rgba(255,255,255,0) 45%, rgba(0,0,0,.06));
  }
  .brand{
    position:absolute;left:34px;top:36px;width:290px;
  }
  .brand-name{
    font-family:"Arimo",Arial,sans-serif;font-weight:700;font-size:22px;
    color:var(--gold);letter-spacing:.3px;white-space:nowrap;
  }
  .brand-line{
    margin-top:6px;display:flex;align-items:center;gap:10px;
  }
  .brand-tagline{
    font-family:"Arimo",Arial,sans-serif;font-size:13px;color:var(--ink);white-space:nowrap;
  }
  .social{display:flex;gap:5px}
  .social-square{
    width:16px;height:16px;border-radius:4px;background:var(--white);
  }
  .crest{
    position:absolute;right:34px;top:26px;width:160px;height:160px;
    border-radius:16px;
    background:radial-gradient(circle at 50% 50%, #4a3510 0%, var(--ink) 55%);
  }
  .person{
    position:absolute;left:34px;top:148px;
  }
  .person-name{
    font-family:"Courgette",cursive;font-size:24px;color:var(--gold);line-height:1;white-space:nowrap;
  }
  .person-role{
    margin-top:6px;
    font-family:"Arimo",Arial,sans-serif;font-weight:700;font-size:13px;color:var(--white);
    letter-spacing:.5px;
  }
  .contact{
    position:absolute;left:34px;top:210px;list-style:none;
    font-family:"Arimo",Arial,sans-serif;font-size:12.5px;color:var(--white);line-height:1.3;
  }
  .contact li{display:flex;align-items:flex-start;gap:8px;margin-bottom:3px}
  .contact svg{flex:none;width:13px;height:13px;margin-top:1px}

  /* back */
  .card-back{background:var(--card-black)}
  .back-pattern{
    position:absolute;inset:0;
    background:
      radial-gradient(ellipse at 0% 100%, rgba(255,255,255,.16) 0%, rgba(255,255,255,0) 55%),
      linear-gradient(35deg, var(--card-black-soft) 0%, var(--card-black-mid) 40%, var(--card-black) 70%, var(--card-black-mid) 100%);
  }
  .back-mark{
    position:absolute;left:62%;top:50%;transform:translate(-50%,-50%);
    font-family:"Arimo",Arial,sans-serif;font-weight:700;font-size:14px;
    color:var(--fuchsia);white-space:nowrap;
  }
</style>
</head>
<body>
<main class="canvas">
  <section class="card card-front">
    <div class="front-texture" role="img" aria-label="Subtle tone-on-tone fuchsia damask pattern"></div>

    <div class="brand">
      <div class="brand-name">The Vixen Rides Again</div>
      <div class="brand-line">
        <span class="brand-tagline">Line of Sparkling Wine &amp; Spirits</span>
        <span class="social" aria-label="Social profiles">
          <span class="social-square"></span>
          <span class="social-square"></span>
        </span>
      </div>
    </div>

    <div class="crest" role="img" aria-label="Ornate black crest with gold monogram"></div>

    <div class="person">
      <div class="person-name">Tara Rose Whitfield</div>
      <div class="person-role">OWNER</div>
    </div>

    <ul class="contact">
      <li>
        <svg viewBox="0 0 14 14" aria-hidden="true"><rect x="3.5" y="1" width="7" height="12" rx="1.5" fill="none" stroke="#f2c21b" stroke-width="1.6"/><circle cx="7" cy="11" r=".8" fill="#f2c21b"/></svg>
        <span>209-555-0143</span>
      </li>
      <li>
        <svg viewBox="0 0 14 14" aria-hidden="true"><path d="M7 13s-4.5-4.6-4.5-7.6A4.5 4.5 0 0 1 11.5 5.4C11.5 8.4 7 13 7 13z" fill="#f2c21b"/><circle cx="7" cy="5.4" r="1.7" fill="#e0158f"/></svg>
        <span>1480 E. Harlow Rd, Bldg. 7, &amp; 8,<br>Lodi Ca. 95299</span>
      </li>
      <li>
        <svg viewBox="0 0 14 14" aria-hidden="true"><circle cx="7" cy="7" r="5.8" fill="none" stroke="#f2c21b" stroke-width="1.4"/><ellipse cx="7" cy="7" rx="2.4" ry="5.8" fill="none" stroke="#f2c21b" stroke-width="1.1"/><line x1="1.2" y1="7" x2="12.8" y2="7" stroke="#f2c21b" stroke-width="1.1"/></svg>
        <span>www.thevixenridesagain.example</span>
      </li>
    </ul>
  </section>

  <section class="card card-back">
    <div class="back-pattern" role="img" aria-label="Black spot-gloss damask crest pattern with a glossy sheen toward the lower left"></div>
    <div class="back-mark">The Vixen Rides Again</div>
  </section>
</main>
</body>
</html>
```